I am planning to launch a new online company called allphonedeskhub.net. This will be a place where people who work in call centres can come and purchase downloadable templates, tool-kits, courseware etc to help them in their jobs. The site will also share the latest information around research, best practices, news in the industry. Essentially a hub for everything call centre related.

I need someone to build the site for me from scratch (I have only just bought the domain name). Everything from the look and feel of the website (focus on easy to use, clean and sharp graphics, with a bit of fun), highly focused on social media and building a community, full blown e-commerce that allows for memberships/subscriptions/and one off purchase models. If you can also design custom graphics (high quality) that would be even better. Given my research of other companies in this space their websites are very dull that look like knowledge bases. I will want alot of cool visuals that attract the customers in. My initial thinking on colour scheme is bright greens/pinks/yellows etc. Not fluorescent though!

The site will contain alot of documents, templates, presentations, videos, articles, white papers etc. You must have experience in the best way to structure the site in an organised manner so that my customer can find what they need very easily.

The person who takes on this work must be happy to work collaboratively with me. It is also key that when the project is delivered that I am able to maintain alot of it myself in terms of uploading documents, blog updates, adding new products, real-time reports/analytics etc.

Whilst you are designing the website I will be working on the content so I will need your help to understand how I structure my content so that it makes sense for the design.

I will base my choice of designer on levels of experience (I will want to see previous work that you have done). I am not adverse to you using tools like shopify etc. if it meets the overall requirements of the site and adds to the functionality/look and feel.

Target Market(s)

People who work in call centres primarily those that are responsible for managing teams of the call centre itself

Industry/Entity Type

Business

Number of Pages Required

5+ page

Font styles to use
Sans Serif

Colors
33b8a4
34a6d7
886aae
b868aa
e667a6
f04a51
f68e4e
faa54b
ffcf3e

Requirements
Must have
• E-commerce functionality that allows for subscriptions and one-off payments
• Credit card processing and accept wire/bank transfers
• Easy to use layout
• Products sold alone and/or as part of bundles
• Membership area
• Front page
• About Us page
• Contact Us page
• Store page (with e-commerce back end)
• News page
• Free Resources page
• Cool, bright, fun look and feel
Nice to have
• Cool, bright, fun graphics
Should not have
• Should not look old fashioned or be difficult to navigate
• Should not look too busy or disorganised

```html
<!DOCTYPE html>
<html lang="en">
<head>
<meta charset="utf-8">
<title>AllPhoneDeskHub</title>
<link href="https://fonts.googleapis.com/css2?family=Open+Sans:wght@400;600&display=swap" rel="stylesheet">
<style>
:root{
  --teal:#33b8a4;--blue:#34a6d7;--violet:#886aae;--plum:#b868aa;--pink:#e667a6;
  --red:#f04a51;--orange:#f68e4e;--amber:#faa54b;--yellow:#ffcf3e;
  --sky:#14a9e6;--ink:#222;--bar:#2a2a2a;--panel:#ececec;--muted:#555;
}
*{margin:0;padding:0;box-sizing:border-box}
html,body{width:1200px;height:769px;overflow:hidden;background:#fff;font-family:"Open Sans",sans-serif;color:var(--ink)}
.page{position:relative;width:1200px;height:769px}
.topline{position:absolute;left:0;top:0;width:1200px;height:3px;background:#d8d8d8}
.brand{position:absolute;left:243px;top:30px;display:flex;align-items:center;gap:10px}
.brand-mark{width:34px;height:34px;background:var(--sky)}
.brand-name{font-size:26px;font-weight:600;color:var(--ink);letter-spacing:.5px}
.contact{position:absolute;left:716px;top:14px;font-size:11.5px;color:#333;display:flex;gap:10px;align-items:center}
.contact span{display:flex;align-items:center;gap:4px}
.sublinks{position:absolute;left:606px;top:45px;font-size:11.5px;letter-spacing:.6px;line-height:20px;color:#333}
.account{position:absolute;left:717px;top:41px;width:254px;height:40px;background:var(--panel);display:flex;align-items:center}
.cart{width:52px;height:100%;display:flex;align-items:center;justify-content:center;border-right:1px solid #d5d5d5}
.login{width:71px;text-align:center;font-size:13px}
.register{width:124px;height:29px;background:var(--sky);color:#fff;font-size:13px;display:flex;align-items:center;justify-content:center;gap:18px;border-radius:2px}
.nav{position:absolute;left:0;top:98px;width:1200px;height:55px;background:var(--bar);border-top:1px solid #ccc;border-bottom:2px solid #ddd}
.nav ul{list-style:none;position:absolute;left:236px;top:17px;display:flex}
.nav li{font-size:14px;letter-spacing:.8px;color:#fff;padding:0 14px;border-left:1px solid #4a4a4a;line-height:20px}
.nav li:first-child{border-left:0}
.nav li.active{color:var(--sky)}
.search{position:absolute;left:805px;top:16px;width:165px;height:24px;background:#fff;border-radius:12px;font-size:10px;font-style:italic;color:#777;padding:6px 8px}
.search svg{position:absolute;right:7px;top:6px}
.hero{position:absolute;left:0;top:155px;width:1200px;height:545px;background:linear-gradient(160deg,#8f959b 0%,#6f757c 45%,#7c7f86 70%,#9a9ea3 100%)}
.tile{position:absolute;width:218px;height:138px;display:flex;align-items:center;justify-content:center;text-align:center;color:#fff;font-size:17.5px;line-height:21.5px;letter-spacing:.2px;opacity:.9}
.tile.featured{border:3px solid #e6e6e6;color:#1f3340;opacity:.92}
.footer{position:absolute;left:0;top:700px;width:1200px;height:69px;background:var(--bar);border-top:3px solid #eee;color:#ddd;font-size:10.5px}
.legal{position:absolute;left:235px;top:30px}
.legal b{color:#fff;font-weight:600}
.pay{position:absolute;left:593px;top:25px;display:flex;align-items:center;gap:11px;color:#fff;font-weight:600}
.card{width:31px;height:19px;border-radius:2px}
.social{position:absolute;left:886px;top:27px;display:flex;gap:5px}
.social i{width:16px;height:16px;border:1.5px solid #aaa;border-radius:50%;display:block}
</style>
</head>
<body>
<div class="page">
  <div class="topline"></div>
  <header>
    <div class="brand"><div class="brand-mark"></div><div class="brand-name">AllPhoneDeskHub</div></div>
    <div class="contact">
      <span><svg width="10" height="10" viewBox="0 0 10 10"><path d="M2 0.5 L3.6 2.8 L2.8 3.8 Q4 6 6.2 7.2 L7.2 6.4 L9.5 8 L8.4 9.5 Q4 9 0.5 1.6 Z" fill="#444"/></svg>555-010-2740</span>
      <span><svg width="10" height="8" viewBox="0 0 10 8"><rect x="0.5" y="0.5" width="9" height="7" fill="#555"/><path d="M0.5 0.5 L5 4.5 L9.5 0.5" stroke="#fff" fill="none"/></svg>info@allphonedeskhub.net</span>
    </div>
    <div class="sublinks">ABOUT US<br>FREE RESOURCES</div>
    <div class="account">
      <div class="cart"><svg width="14" height="12" viewBox="0 0 14 12"><path d="M0.5 1 H3 L4.5 8 H12 L13 3 H3.6" stroke="#333" stroke-width="1.4" fill="none"/><circle cx="5.5" cy="10.5" r="1.1" fill="#333"/><circle cx="11" cy="10.5" r="1.1" fill="#333"/></svg></div>
      <div class="login">LOGIN</div>
      <div class="register">REGISTER <svg width="7" height="10" viewBox="0 0 7 10"><path d="M1 1 L5.5 5 L1 9" stroke="#1a1a1a" stroke-width="2" fill="none"/></svg></div>
    </div>
  </header>
  <nav class="nav">
    <ul>
      <li class="active">HOME</li><li>NEWS</li><li>FREE STUFF</li><li>MEMBERSHIP</li><li>CONTACT US</li>
    </ul>
    <div class="search">Search<svg width="11" height="11" viewBox="0 0 11 11"><circle cx="4.5" cy="4.5" r="3.5" stroke="#444" stroke-width="1.4" fill="none"/><path d="M7 7 L10 10" stroke="#444" stroke-width="1.6"/></svg></div>
  </nav>
  <main class="hero" role="img" aria-label="Background photo of silhouetted people working in a bright open-plan office">
    <div class="tile" style="left:252px;top:34px;background:var(--teal)">PERFORMANCE<br>MEASUREMENT<br>&amp; MANAGEMENT</div>
    <div class="tile featured" style="left:495px;top:33px;width:220px;height:140px;background:var(--blue)">MORAL &amp;<br>MOTIVATION</div>
    <div class="tile" style="left:740px;top:34px;background:var(--violet)">COACHING<br>&amp; MENTORING</div>
    <div class="tile" style="left:252px;top:196px;background:var(--plum)">LEADERSHIP<br>&amp; MANAGEMENT</div>
    <div class="tile" style="left:496px;top:196px;background:var(--pink)">REWARD<br>&amp; RECOGNITION</div>
    <div class="tile" style="left:740px;top:196px;background:var(--red)">COMMUNICATION<br>SKILLS</div>
    <div class="tile" style="left:252px;top:358px;background:var(--orange)">CALL CENTER<br>TECHNOLOGY</div>
    <div class="tile" style="left:496px;top:358px;background:var(--amber)">CALL CENTER<br>STRATEGY</div>
    <div class="tile" style="left:740px;top:358px;background:var(--yellow)">RESEARCH &amp;<br>BEST PRACTICES</div>
  </main>
  <footer class="footer">
    <div class="legal">© 2015. <b>AllPhoneDeskHub</b> &nbsp;| &nbsp;Privacy Policy &nbsp;| &nbsp;Terms &amp; Conditions</div>
    <div class="pay">We Accept :
      <span class="card" style="background:#f2f2f2"></span>
      <span class="card" style="background:#1d3f73"></span>
      <span class="card" style="background:#111;border:1px solid #555"></span>
      <span class="card" style="background:#f4d27a"></span>
    </div>
    <div class="social"><i></i><i></i><i></i><i></i></div>
  </footer>
</div>
</body>
</html>
```